Background on the company
=======================
This is a Bitcoin Consulting Company.

We have two projects.

Tinted Tokens: software to trade assets over the Bitcoin protocol (assets like property, traditional currencies, gold, stocks, securities, bonds, etc.).

Quarnix Private Vaulter: a hardware based web service in a box that manages cold storage wallets and off line transaction signing. It is the secure way to deploy a web wallet without relying on third parties.

All that to say this is a high tech company focusing on Bitcoin.

What does Fellowdrim mean?
========================

The Beast of Fellowdrim is the rabbit in Jasper Quill's Silver Chalice that defeats his band of knights. (At least until they go and get the Sacred Pocket Rocket).

We like this, because we are a deceptively soft and fuzzy company that is also killer!

What We Need:
============

Primarily we need to get the logo designed. I have a hand drawing I did, but you are not limited to that. And the logo needs to work on a business card. The right logo that works on a Business Card is the primary consideration.
Updates

The main task here is to get the logo right.  I have provided a drawing I made, and I like it, but my complaints are:  Fellowdrim is hard to read.  The 'C' isn't obvious.

We can fix this many ways.  We can forget the whole "combinde a rabit with the C and a" idea.  We can add "Fellowdrim Systems" on the card apart from the logo (that way if they don't "get it" they can still read it.)

The Rabbit itself is quite obviously scanned from a hand drawing.  That might not be a bad thing, but combine that with the entire logo, and it is too cheap looking.

Target Market(s)

Technical folks. Investors. Business contacts.

Industry/Entity Type

Software

Requirements
Must have
• We have to clean up the logo, or replace it with something that hints at the same sort of things. (See the upload) Basically and innocent white bunny. Something that works on a Business Card.

All the information below:

Derek Haldane
ph (555) 304-1927
haldane.derek@mailvista.example
derek@fellowdrim.example
Nice to have
• I would like it to be serious, yet whimsical. An inside joke, so you get it if you know Jasper Quill. But otherwise, it looks reasonably serious if you don't know Jasper Quill.

I don't want it to be scary. (oddly, that my own efforts seem to make that easy to do)

Would like a set of colors that remind one of a cave, a rabbit, knights.... Not sure what those are...

```html
<!DOCTYPE html>
<html lang="en">
<head>
<meta charset="utf-8">
<title>Fellowdrim Business Card</title>
<link rel="stylesheet" href="https://fonts.googleapis.com/css2?family=Arimo:wght@400;700&display=swap">
<style>
  :root {
    --backdrop: #d8d8d8;
    --card-white: #ffffff;
    --brand-orange: #f18d05;
    --charcoal: #26282a;
    --charcoal-deep: #1a1b1d;
    --wordmark-grey: #343434;
    --contact-white: #f4f4f4;
  }
  * { margin: 0; padding: 0; box-sizing: border-box; }
  html, body {
    width: 1200px;
    height: 900px;
    overflow: hidden;
    background: var(--backdrop);
    font-family: "Arimo", Arial, sans-serif;
  }
  .stage {
    width: 1200px;
    height: 900px;
    display: flex;
    align-items: center;
    justify-content: center;
  }
  .business-card {
    position: relative;
    width: 1000px;
    height: 572px;
    border-radius: 44px;
    overflow: hidden;
    background: var(--card-white);
    box-shadow: 0 18px 40px rgba(0, 0, 0, 0.25);
  }
  .brand-area {
    height: 292px;
    display: flex;
    align-items: center;
    padding-left: 110px;
    gap: 26px;
  }
  .brand-dot {
    width: 70px;
    height: 70px;
    border-radius: 50%;
    background: var(--brand-orange);
    flex: none;
  }
  .wordmark {
    font-family: "Arimo", Arial, sans-serif;
    font-weight: 700;
    font-size: 112px;
    letter-spacing: -2px;
    color: var(--wordmark-grey);
    line-height: 1;
  }
  .accent-rule {
    height: 12px;
    background: var(--brand-orange);
  }
  .contact-panel {
    height: 268px;
    background: linear-gradient(180deg, var(--charcoal) 0%, var(--charcoal-deep) 100%);
    padding: 40px 0 0 60px;
  }
  .holder-name {
    font-weight: 700;
    font-size: 40px;
    color: var(--brand-orange);
    margin-bottom: 22px;
  }
  .contact-list {
    list-style: none;
  }
  .contact-item {
    display: flex;
    align-items: center;
    gap: 12px;
    font-size: 38px;
    color: var(--contact-white);
    line-height: 1;
    margin-bottom: 14px;
  }
  .contact-icon {
    width: 36px;
    height: 36px;
    flex: none;
  }
</style>
</head>
<body>
<main class="stage">
  <article class="business-card">
    <header class="brand-area">
      <span class="brand-dot"></span>
      <span class="wordmark">Fellowdrim</span>
    </header>
    <div class="accent-rule"></div>
    <section class="contact-panel">
      <h1 class="holder-name">Derek Haldane</h1>
      <ul class="contact-list">
        <li class="contact-item">
          <svg class="contact-icon" viewBox="0 0 24 24" aria-hidden="true">
            <path fill="#f18d05" d="M6.6 10.8a15.2 15.2 0 0 0 6.6 6.6l2.2-2.2a1 1 0 0 1 1-.25 11.4 11.4 0 0 0 3.6.57 1 1 0 0 1 1 1V20a1 1 0 0 1-1 1A17 17 0 0 1 3 4a1 1 0 0 1 1-1h3.5a1 1 0 0 1 1 1c0 1.25.2 2.45.57 3.57a1 1 0 0 1-.25 1z"/>
          </svg>
          <span>(555) 304-1927</span>
        </li>
        <li class="contact-item">
          <svg class="contact-icon" viewBox="0 0 24 24" aria-hidden="true">
            <rect x="2" y="5" width="20" height="14" rx="1.5" fill="#f18d05"/>
            <path d="M3 6.5l9 6.5 9-6.5" fill="none" stroke="#26282a" stroke-width="1.6"/>
          </svg>
          <span>haldane.derek@mailvista.example</span>
        </li>
        <li class="contact-item">
          <svg class="contact-icon" viewBox="0 0 24 24" aria-hidden="true">
            <rect x="2" y="5" width="20" height="14" rx="1.5" fill="#f18d05"/>
            <path d="M3 6.5l9 6.5 9-6.5" fill="none" stroke="#26282a" stroke-width="1.6"/>
          </svg>
          <span>derek@fellowdrim.example</span>
        </li>
      </ul>
    </section>
  </article>
</main>
</body>
</html>
```